Business Card Design For Office Furniture Clearance Company

Kestrel Office Clearance - our company name pretty much explains what we do, we clear offices for high end clients, mainly plc's and large international companies.

We require a nice looking business card that displays professionalism but without being too serious.

It would be nice to see just a little more than a conventional boring business card, make sure you add some flare.

Industry/Entity Type

Office Furniture

Contact Information for Business Card

CARD 1

Mark Holloway
Director
mark@kestrelofficeclear.co.uk
m: 07700 913528

t: 01632 960418
www.kestrelofficeclear.co.uk

Kestrel Office Clearance
Unit K4 B
3-7 Fenwick Lane
Harwood
Castlebrook
ZX9 4QT

free office clearances… you cant get better than that.

CARD 2

Peter Donaldson
Director
peter@kestrelofficeclear.co.uk
m: 07700 927153

t: 01632 960418

Kestrel Office Clearance
Unit K4 B
3-7 Fenwick Lane
Harwood
Castlebrook
ZX9 4QT

Font styles to use
Sans Serif

Requirements
Must have
• A white background - as we have a blue logo.
Nice to have
• Nice use of the logo - play around with this and dissect it.

```html
<!DOCTYPE html>
<html lang="en">
<head>
<meta charset="utf-8">
<title>Kestrel Office Clearance – Business Cards</title>
<link rel="stylesheet" href="https://fonts.googleapis.com/css2?family=Open+Sans:wght@400;600&family=Questrial&display=swap">
<style>
  :root {
    --bg: #26282b;
    --card-white: #f6f7f9;
    --brand-blue: #1a7bbf;
    --brand-blue-deep: #1f6a9e;
    --ink: #1b1d20;
    --ink-soft: #3a3d42;
    --paper-white: #ffffff;
  }
  * { box-sizing: border-box; margin: 0; padding: 0; }
  html, body {
    width: 1200px; height: 1200px; overflow: hidden;
    background: var(--bg);
  }
  .canvas { position: relative; width: 1200px; height: 1200px; }
  .defs { position: absolute; width: 0; height: 0; }

  .card {
    position: absolute;
    width: 540px; height: 350px;
    overflow: hidden;
    background: var(--card-white);
    box-shadow: 0 18px 40px rgba(0,0,0,.45);
  }
  .card--mark  { left: 40px;  top: 200px; }
  .card--peter { left: 620px; top: 200px; }
  .card--back  { left: 330px; top: 650px; }

  .card__art { position: absolute; inset: 0; width: 100%; height: 100%; display: block; }

  .card__name-block {
    position: absolute; left: 28px; top: 24px;
    padding-left: 14px;
    border-left: 6px solid var(--ink);
  }
  .card__name {
    font-family: "Questrial", sans-serif;
    font-size: 30px; line-height: 32px; color: var(--ink);
  }
  .card__role {
    font-family: "Questrial", sans-serif;
    font-size: 17px; line-height: 18px; color: var(--ink-soft);
  }

  .contact-row {
    position: absolute; left: 40px;
    display: flex; align-items: center; gap: 12px;
  }
  .contact-row--phone   { top: 86px; }
  .contact-row--web     { top: 143px; }
  .contact-row--address { top: 196px; align-items: flex-start; }

  .contact-icon {
    width: 38px; height: 38px; border-radius: 8px;
    background: var(--brand-blue);
    display: flex; align-items: center; justify-content: center;
    flex: none;
  }
  .contact-icon svg { width: 22px; height: 22px; }
  .contact-icon--light { background: var(--paper-white); }

  .contact-text {
    font-family: "Open Sans", sans-serif;
    font-size: 13px; line-height: 17px; color: var(--ink);
  }
  .contact-text--phone { font-size: 14px; line-height: 18px; letter-spacing: .3px; }
  .contact-text--web { color: var(--paper-white); font-size: 12.5px; }
  .contact-text--address { font-size: 11.5px; line-height: 15px; }

  .brand-mark {
    position: absolute;
    display: flex; align-items: center; gap: 8px;
    font-family: "Open Sans", sans-serif; font-weight: 600;
    color: var(--paper-white);
    white-space: nowrap;
  }
  .brand-mark__dot {
    border-radius: 50%; background: var(--paper-white); flex: none;
  }
  .card--mark .brand-mark,
  .card--peter .brand-mark { right: 22px; bottom: 38px; font-size: 13px; }
  .card--mark .brand-mark__dot,
  .card--peter .brand-mark__dot { width: 16px; height: 16px; }
  .card--back .brand-mark { right: 40px; bottom: 74px; font-size: 19px; gap: 12px; }
  .card--back .brand-mark__dot { width: 26px; height: 26px; }
</style>
</head>
<body>
<main class="canvas">

  <svg class="defs" aria-hidden="true">
    <defs>
      <linearGradient id="office-photo" x1="0" y1="0" x2="1" y2="1">
        <stop offset="0" stop-color="#8f8a7c"/>
        <stop offset=".45" stop-color="#d9d6cb"/>
        <stop offset=".7" stop-color="#eef0ee"/>
        <stop offset="1" stop-color="#b9bcb6"/>
      </linearGradient>
      <linearGradient id="blue-overlay" x1="0" y1="0" x2="1" y2="1">
        <stop offset="0" stop-color="#1f6a9e" stop-opacity=".9"/>
        <stop offset="1" stop-color="#4d9fd2" stop-opacity=".85"/>
      </linearGradient>
    </defs>
  </svg>

  <article class="card card--mark">
    <svg class="card__art" viewBox="0 0 540 350" preserveAspectRatio="none">
      <polygon points="420,0 540,0 540,350 230,350" fill="url(#office-photo)" role="img" aria-label="Photograph of a bright, empty office interior with tall windows"/>
      <polygon points="290,240 540,240 540,350 230,350" fill="url(#blue-overlay)"/>
      <line x1="420" y1="0" x2="230" y2="350" stroke="var(--brand-blue)" stroke-width="3"/>
      <polygon points="0,138 392,138 372,186 0,186" fill="var(--brand-blue)"/>
    </svg>

    <div class="card__name-block">
      <h2 class="card__name">Mark Holloway</h2>
      <p class="card__role">Director</p>
    </div>

    <div class="contact-row contact-row--phone">
      <span class="contact-icon">
        <svg viewBox="0 0 24 24" fill="none" stroke="#fff" stroke-width="2" stroke-linecap="round" stroke-linejoin="round"><path d="M5 3h4l2 5-2.5 1.5a11 11 0 0 0 6 6L16 13l5 2v4a2 2 0 0 1-2 2A16 16 0 0 1 3 5a2 2 0 0 1 2-2z"/></svg>
      </span>
      <p class="contact-text contact-text--phone">07700 913528<br>01632 960418</p>
    </div>

    <div class="contact-row contact-row--web">
      <span class="contact-icon contact-icon--light">
        <svg viewBox="0 0 24 24" fill="none" stroke="#1a7bbf" stroke-width="1.6"><circle cx="12" cy="12" r="9"/><ellipse cx="12" cy="12" rx="4" ry="9"/><path d="M3 12h18M4.5 7.5h15M4.5 16.5h15"/></svg>
      </span>
      <p class="contact-text contact-text--web">mark@kestrelofficeclear.co.uk<br>www.kestrelofficeclear.co.uk</p>
    </div>

    <div class="contact-row contact-row--address">
      <span class="contact-icon">
        <svg viewBox="0 0 24 24" fill="none" stroke="#fff" stroke-width="2"><path d="M12 22s-7-7.5-7-12a7 7 0 0 1 14 0c0 4.5-7 12-7 12z"/><circle cx="12" cy="10" r="2.6"/></svg>
      </span>
      <p class="contact-text contact-text--address">Kestrel Office Clearance, Unit K4 B<br>3-7 Fenwick Lane, Harwood<br>Castlebrook, ZX9 4QT</p>
    </div>

    <div class="brand-mark"><span class="brand-mark__dot"></span>Kestrel Office Clearance</div>
  </article>

  <article class="card card--peter">
    <svg class="card__art" viewBox="0 0 540 350" preserveAspectRatio="none">
      <polygon points="420,0 540,0 540,350 230,350" fill="url(#office-photo)" role="img" aria-label="Photograph of a bright, empty office interior with tall windows"/>
      <polygon points="290,240 540,240 540,350 230,350" fill="url(#blue-overlay)"/>
      <line x1="420" y1="0" x2="230" y2="350" stroke="var(--brand-blue)" stroke-width="3"/>
      <polygon points="0,138 392,138 372,186 0,186" fill="var(--brand-blue)"/>
    </svg>

    <div class="card__name-block">
      <h2 class="card__name">Peter Donaldson</h2>
      <p class="card__role">Director</p>
    </div>

    <div class="contact-row contact-row--phone">
      <span class="contact-icon">
        <svg viewBox="0 0 24 24" fill="none" stroke="#fff" stroke-width="2" stroke-linecap="round" stroke-linejoin="round"><path d="M5 3h4l2 5-2.5 1.5a11 11 0 0 0 6 6L16 13l5 2v4a2 2 0 0 1-2 2A16 16 0 0 1 3 5a2 2 0 0 1 2-2z"/></svg>
      </span>
      <p class="contact-text contact-text--phone">07700 927153<br>01632 960418</p>
    </div>

    <div class="contact-row contact-row--web">
      <span class="contact-icon contact-icon--light">
        <svg viewBox="0 0 24 24" fill="none" stroke="#1a7bbf" stroke-width="1.6"><circle cx="12" cy="12" r="9"/><ellipse cx="12" cy="12" rx="4" ry="9"/><path d="M3 12h18M4.5 7.5h15M4.5 16.5h15"/></svg>
      </span>
      <p class="contact-text contact-text--web">peter@kestrelofficeclear.co.uk<br>www.kestrelofficeclear.co.uk</p>
    </div>

    <div class="contact-row contact-row--address">
      <span class="contact-icon">
        <svg viewBox="0 0 24 24" fill="none" stroke="#fff" stroke-width="2"><path d="M12 22s-7-7.5-7-12a7 7 0 0 1 14 0c0 4.5-7 12-7 12z"/><circle cx="12" cy="10" r="2.6"/></svg>
      </span>
      <p class="contact-text contact-text--address">Kestrel Office Clearance, Unit K4 B<br>3-7 Fenwick Lane, Harwood<br>Castlebrook, ZX9 4QT</p>
    </div>

    <div class="brand-mark"><span class="brand-mark__dot"></span>Kestrel Office Clearance</div>
  </article>

  <article class="card card--back">
    <svg class="card__art" viewBox="0 0 540 350" preserveAspectRatio="none">
      <rect width="540" height="350" fill="url(#office-photo)" role="img" aria-label="Photograph of a bright, empty office interior with tall windows and a city view"/>
      <rect y="160" width="540" height="190" fill="url(#blue-overlay)"/>
    </svg>
    <div class="brand-mark"><span class="brand-mark__dot"></span>Kestrel Office Clearance</div>
  </article>

</main>
</body>
</html>
```